Lifestyle blog needs a website

I have a blog called Bright Years Ahead. Logo has been done and I also have the wordpress site with a theme already added to it.

The basics are there but I need design expertise to put everything together, make it look great and ready for me to go and in and start using. Basically what is there at the moment needs to be deleted and start again (not a lot - just me playing around). I am not attached to the theme and am happy to go with whatever ideas you can come up with. At the moment I am looking at 3 lifestyle categories (Fashion, Fitness, Feelings) with a contact page so not an extensive build.

Audience will be women over 40 but please don't make this 'frumpy' - it is aimed at the women who act, look and feel younger than their age and so 'pink & fluffy' and 'old & solid' is not the look I am going for.

My deepest apologies for the delay in responding to designs. I had a family matter which took meant I was unable to spend the quality time required to review. I will therefore be reviewing and deciding over this weekend. Once again, my sincere apologies.

Women over 40

• Feeling of being targeted at old market

```html
<!DOCTYPE html>
<html lang="en">
<head>
<meta charset="utf-8">
<title>Bright Years Ahead — Fashion, Fitness, Feelings</title>
<link href="https://fonts.googleapis.com/css2?family=Oswald:wght@400;500&family=Open+Sans:wght@400;600&display=swap" rel="stylesheet">
<style>
:root{
  --red:#e5323b;
  --orange:#df8a2b;
  --teal:#1fb28a;
  --blue:#2a9fd8;
  --ink:#222;
  --body:#555;
  --muted:#888;
  --light:#f4f4f4;
  --dark:#2a2a2a;
  --white:#fff;
}
*{margin:0;padding:0;box-sizing:border-box}
html,body{width:1200px;height:3429px;overflow:hidden}
body{position:relative;font-family:"Open Sans",Arial,sans-serif;color:var(--body);background:var(--white)}
.abs{position:absolute}

/* header */
.site-header{position:absolute;top:0;left:0;width:1200px;height:110px;background:var(--white);z-index:3}
.brand{position:absolute;left:88px;top:8px;width:156px;height:156px;border-radius:50%;background:var(--white);box-shadow:0 4px 14px rgba(0,0,0,.18);display:flex;align-items:center;justify-content:center;text-align:center;z-index:4}
.brand span{font-family:"Oswald",sans-serif;font-weight:500;color:var(--red);font-size:25px;line-height:1.05;text-transform:uppercase}
.main-nav{position:absolute;right:92px;top:38px;display:flex;align-items:center;gap:38px;font-size:17px;color:var(--ink)}
.main-nav .active{color:var(--red)}
.nav-contact{background:var(--red);color:var(--white);padding:10px 22px;font-size:15px;text-transform:uppercase;border-radius:2px}

/* hero */
.hero{position:absolute;top:110px;left:0;width:1200px;height:650px}
.hero-photo{position:absolute;inset:0;background:linear-gradient(100deg,#d7e6ee 0%,#e6eef0 35%,#cfb79a 60%,#b58a66 80%,#e5dccf 100%)}
.hero-cut{position:absolute;left:0;top:0;width:1200px;height:650px}
.hero-title{position:absolute;left:91px;top:200px;font-family:"Oswald",sans-serif;color:var(--red);font-size:66px;font-weight:500;line-height:1;text-transform:uppercase}
.hero-sub{position:absolute;left:91px;top:290px;font-family:"Oswald",sans-serif;color:var(--ink);font-size:36px;font-weight:400}
.hero-arrows{position:absolute;left:91px;top:362px;display:flex;gap:8px}
.hero-arrows span{width:28px;height:28px;border-radius:50%;background:#777;display:flex;align-items:center;justify-content:center}

.section-title{position:absolute;left:0;width:1200px;text-align:center;font-size:36px;font-weight:400;color:var(--ink);text-transform:uppercase}

/* about */
.about-text{position:absolute;left:152px;top:882px;width:896px;text-align:center;font-size:15px;line-height:26px;color:var(--body)}
.btn{display:inline-block;background:var(--red);color:var(--white);border-radius:20px;font-size:15px;padding:8px 26px}

/* fashion */
.fashion{position:absolute;top:1115px;left:0;width:1200px;height:547px;background:var(--orange)}
.fashion .section-title{color:var(--white);top:62px}
.fashion-card{position:absolute;top:154px;width:240px;height:324px;background:var(--white)}
.fashion-card .photo{height:210px}
.fashion-card .badge{position:absolute;right:10px;top:190px;width:42px;height:42px;border-radius:50%;background:#f0a23b;border:3px solid var(--white);display:flex;align-items:center;justify-content:center}
.fashion-card h3{margin:22px 0 0 20px;font-size:15px;font-weight:400;color:var(--ink);text-transform:uppercase}
.fashion-card p{margin:12px 20px 0;font-size:13.5px;line-height:22px;color:var(--muted)}

/* fitness */
.fit-feature{position:absolute;left:91px;top:1879px;width:499px;height:464px;background:linear-gradient(160deg,#eee3d6 0%,#cfc3b5 45%,#7a6b5f 100%)}
.fit-feature .shade{position:absolute;left:0;bottom:0;width:100%;height:150px;background:linear-gradient(transparent,rgba(0,0,0,.55))}
.fit-feature .caption{position:absolute;left:34px;bottom:86px;color:var(--white);font-size:17px}
.fit-feature .tag{position:absolute;left:34px;bottom:28px;display:flex;align-items:center;gap:12px;color:var(--white);font-size:16px}
.fit-feature .meta{position:absolute;right:34px;bottom:32px;display:flex;gap:18px}
.icon-dot{width:40px;height:40px;border-radius:50%;background:var(--teal);display:flex;align-items:center;justify-content:center}
.fit-item{position:absolute;left:631px;width:480px;height:160px;border-bottom:1px solid #e3e3e3}
.fit-item .thumb{position:absolute;left:2px;top:6px;width:183px;height:125px}
.fit-item .icon-dot{position:absolute;left:160px;top:48px;border:3px solid var(--white);width:44px;height:44px}
.fit-item h3{position:absolute;left:230px;top:10px;font-size:17px;font-weight:400;color:var(--ink)}
.fit-item p{position:absolute;left:230px;top:40px;width:250px;font-size:13.5px;line-height:26px;color:var(--body)}
.fit-item .meta{position:absolute;left:230px;top:104px;display:flex;gap:14px}

/* feelings */
.feelings{position:absolute;top:2453px;left:0;width:1200px;height:546px;background:var(--light)}
.feel-card{position:absolute;top:148px;width:311px}
.feel-card .photo{height:174px;position:relative}
.feel-card .smile{position:absolute;right:10px;top:148px;width:48px;height:48px;border-radius:50%;background:var(--blue);border:3px solid var(--white);display:flex;align-items:center;justify-content:center}
.feel-meta{display:flex;margin-top:22px;height:22px;font-size:12px}
.feel-meta .date{background:var(--blue);color:var(--white);padding:3px 12px}
.feel-meta .count{background:#333;width:38px;display:flex;align-items:center;justify-content:center}
.feel-card h3{margin-top:16px;font-size:16px;font-weight:400;color:var(--ink)}
.feel-card p{margin-top:10px;font-size:13px;line-height:21px;color:var(--muted)}
.feel-card a{display:block;margin-top:10px;font-size:13px;color:var(--blue);text-decoration:none}

/* footer */
.site-footer{position:absolute;top:2999px;left:0;width:1200px;height:430px;background:linear-gradient(#333,#1f1f1f);color:#ddd}
.newsletter{position:absolute;left:262px;top:56px;display:flex;align-items:center}
.newsletter h2{font-size:36px;font-weight:400;color:var(--white);margin-right:40px}
.newsletter .field{width:346px;height:44px;background:var(--white);border-radius:22px 0 0 22px;font-size:12px;color:#aaa;padding:14px 22px}
.newsletter .submit{height:44px;background:var(--red);color:var(--white);font-size:13px;padding:13px 20px;border-radius:0 22px 22px 0}
.footer-brand{position:absolute;left:120px;top:200px;font-family:"Oswald",sans-serif;font-weight:500;color:var(--white);font-size:30px;line-height:1.1;text-transform:uppercase}
.footer-col{position:absolute;top:190px}
.footer-col h4{font-size:14px;font-weight:400;color:var(--white);text-transform:uppercase;margin-bottom:18px}
.footer-col li{list-style:none;font-size:12px;line-height:25px;color:#ccc}
.footer-col li::before{content:"» ";}
.footer-col p{font-size:12px;line-height:25px;color:#ccc}
.social{display:flex;gap:10px}
.social span{width:30px;height:30px;border-radius:50%;background:var(--white)}
.footer-rule{position:absolute;left:120px;top:343px;width:960px;height:1px;background:#444}
.copyright{position:absolute;left:0;top:373px;width:1200px;text-align:center;font-size:13px;color:#ddd}
</style>
</head>
<body>

<header class="site-header">
  <nav class="main-nav">
    <span class="active">Home</span><span>About us</span><span>Fashion</span><span>Fitness</span><span>Feelings</span><span class="nav-contact">Contact</span>
  </nav>
</header>
<div class="brand"><span>Bright<br>Years<br>Ahead</span></div>

<section class="hero">
  <div class="hero-photo" role="img" aria-label="Sunny outdoor photo of a laughing couple in sunglasses, the woman riding piggyback"></div>
  <svg class="hero-cut" viewBox="0 0 1200 650" aria-hidden="true">
    <polygon points="0,507 549,645 1200,507 1200,650 0,650" fill="#fff"/>
    <polyline points="0,507 549,645 1200,507" fill="none" stroke="#e5323b" stroke-width="5"/>
  </svg>
  <div class="hero-title">Bright Years Ahead</div>
  <div class="hero-sub">Fashion, Fitness, Feelings</div>
  <div class="hero-arrows">
    <span><svg width="12" height="12" viewBox="0 0 12 12"><path d="M8 2 4 6l4 4" stroke="#fff" stroke-width="2" fill="none"/></svg></span>
    <span><svg width="12" height="12" viewBox="0 0 12 12"><path d="M4 2l4 4-4 4" stroke="#fff" stroke-width="2" fill="none"/></svg></span>
  </div>
</section>

<h2 class="section-title" style="top:822px">About Us</h2>
<p class="about-text">It is a long established fact that a reader will be distracted by the readable content of a page when looking at its layout. The point of using Lorem Ipsum is that it has a more-or-less normal distribution of letters, as opposed to using 'Content here, content here', making it look like readable English It is a long established fact that a reader will be distracted by the readable content of a page when looking at its layout. The point of using here', making it look like readable English</p>
<div class="abs" style="top:1006px;left:0;width:1200px;text-align:center"><span class="btn">Read More</span></div>

<section class="fashion">
  <h2 class="section-title">Fashion</h2>
  <article class="fashion-card" style="left:91px">
    <div class="photo" role="img" aria-label="Man in a blue suit and sunglasses holding a coffee" style="background:linear-gradient(160deg,#a8b3bd,#3d5670)"></div>
    <div class="badge"><svg width="16" height="16" viewBox="0 0 16 16"><circle cx="8" cy="5" r="3.2" fill="#fff"/><path d="M2 15c0-4 3-6 6-6s6 2 6 6z" fill="#fff"/></svg></div>
    <h3>Porro Quisquam</h3><p>Simply dummy text of the printing and type page</p>
  </article>
  <article class="fashion-card" style="left:350px">
    <div class="photo" role="img" aria-label="Woman in a sun hat with shopping bags" style="background:linear-gradient(160deg,#e7d9c8,#b69a86)"></div>
    <div class="badge"><svg width="16" height="16" viewBox="0 0 16 16"><circle cx="8" cy="5" r="3.2" fill="#fff"/><path d="M2 15c0-4 3-6 6-6s6 2 6 6z" fill="#fff"/></svg></div>
    <h3>Dolorem Ipsum</h3><p>Ipsum is simply dummy text printing and type page</p>
  </article>
  <article class="fashion-card" style="left:610px">
    <div class="photo" role="img" aria-label="Man in sunglasses and white shirt on a city street" style="background:linear-gradient(160deg,#5d7fa6,#c9b8a6)"></div>
    <div class="badge"><svg width="16" height="16" viewBox="0 0 16 16"><circle cx="8" cy="5" r="3.2" fill="#fff"/><path d="M2 15c0-4 3-6 6-6s6 2 6 6z" fill="#fff"/></svg></div>
    <h3>Neque Porro</h3><p>Simply dummy text of the printing and type page</p>
  </article>
  <article class="fashion-card" style="left:871px">
    <div class="photo" role="img" aria-label="Woman in a red top walking through town" style="background:linear-gradient(160deg,#c7b7a5,#8a7566)"></div>
    <div class="badge"><svg width="16" height="16" viewBox="0 0 16 16"><circle cx="8" cy="5" r="3.2" fill="#fff"/><path d="M2 15c0-4 3-6 6-6s6 2 6 6z" fill="#fff"/></svg></div>
    <h3>Quisquam Dolorem</h3><p>Ipsum is simply dummy text printing and type page</p>
  </article>
</section>

<h2 class="section-title" style="top:1774px">Fitness</h2>
<article class="fit-feature" role="img" aria-label="Woman in sportswear drinking from a bottle in a bright kitchen">
  <div class="shade"></div>
  <div class="caption">Neque porro quisquam est qui dolorem</div>
  <div class="tag"><span class="icon-dot"><svg width="18" height="18" viewBox="0 0 18 18"><circle cx="11" cy="3" r="2" fill="#fff"/><path d="M4 8l4-3 3 3 3 1M8 5l-1 6 4 2-1 4M7 11l-3 5" stroke="#fff" stroke-width="1.8" fill="none"/></svg></span>Fitness</div>
  <div class="meta">
    <svg width="20" height="20" viewBox="0 0 20 20"><circle cx="10" cy="6" r="4" fill="none" stroke="#fff" stroke-width="1.5"/><path d="M3 19c0-5 3-7 7-7s7 2 7 7" fill="none" stroke="#fff" stroke-width="1.5"/></svg>
    <svg width="20" height="20" viewBox="0 0 20 20"><rect x="2" y="4" width="16" height="14" fill="none" stroke="#fff" stroke-width="1.5"/><path d="M2 8h16M6 2v4M14 2v4" stroke="#fff" stroke-width="1.5"/></svg>
    <svg width="20" height="20" viewBox="0 0 20 20"><rect x="2" y="3" width="16" height="11" fill="none" stroke="#fff" stroke-width="1.5"/><path d="M6 14l-2 4 5-4" fill="none" stroke="#fff" stroke-width="1.5"/></svg>
  </div>
</article>

<article class="fit-item" style="top:1879px">
  <div class="thumb" role="img" aria-label="Woman eating a fresh salad" style="background:linear-gradient(150deg,#e8e2da,#b9a48f)"></div>
  <span class="icon-dot"><svg width="18" height="18" viewBox="0 0 18 18"><circle cx="11" cy="3" r="2" fill="#fff"/><path d="M4 8l4-3 3 3 3 1M8 5l-1 6 4 2-1 4M7 11l-3 5" stroke="#fff" stroke-width="1.8" fill="none"/></svg></span>
  <h3>Neque porro quisquam est</h3><p>Ipsum is simply dummy text of the printing and type page when</p>
  <div class="meta"><svg width="18" height="18" viewBox="0 0 20 20"><path d="M10 2l2.4 5.2 5.6.6-4.2 3.8 1.2 5.6L10 14.4 5 17.2l1.2-5.6L2 7.8l5.6-.6z" fill="none" stroke="#999" stroke-width="1.4"/></svg><svg width="18" height="18" viewBox="0 0 20 20"><rect x="2" y="4" width="16" height="14" fill="none" stroke="#999" stroke-width="1.4"/><path d="M2 8h16" stroke="#999" stroke-width="1.4"/></svg><svg width="18" height="18" viewBox="0 0 20 20"><circle cx="10" cy="6" r="4" fill="none" stroke="#999" stroke-width="1.4"/><path d="M3 19c0-5 3-7 7-7s7 2 7 7" fill="none" stroke="#999" stroke-width="1.4"/></svg></div>
</article>
<article class="fit-item" style="top:2039px">
  <div class="thumb" role="img" aria-label="Woman running on a bridge" style="background:linear-gradient(150deg,#6f7780,#c9ccd0)"></div>
  <span class="icon-dot"><svg width="18" height="18" viewBox="0 0 18 18"><circle cx="11" cy="3" r="2" fill="#fff"/><path d="M4 8l4-3 3 3 3 1M8 5l-1 6 4 2-1 4M7 11l-3 5" stroke="#fff" stroke-width="1.8" fill="none"/></svg></span>
  <h3>Porro quisquam est dolorem</h3><p>Ipsum is simply dummy text of the printing and type page when</p>
  <div class="meta"><svg width="18" height="18" viewBox="0 0 20 20"><path d="M10 2l2.4 5.2 5.6.6-4.2 3.8 1.2 5.6L10 14.4 5 17.2l1.2-5.6L2 7.8l5.6-.6z" fill="none" stroke="#999" stroke-width="1.4"/></svg><svg width="18" height="18" viewBox="0 0 20 20"><rect x="2" y="4" width="16" height="14" fill="none" stroke="#999" stroke-width="1.4"/><path d="M2 8h16" stroke="#999" stroke-width="1.4"/></svg><svg width="18" height="18" viewBox="0 0 20 20"><circle cx="10" cy="6" r="4" fill="none" stroke="#999" stroke-width="1.4"/><path d="M3 19c0-5 3-7 7-7s7 2 7 7" fill="none" stroke="#999" stroke-width="1.4"/></svg></div>
</article>
<article class="fit-item" style="top:2199px">
  <div class="thumb" role="img" aria-label="Man jogging outdoors in warm light" style="background:linear-gradient(150deg,#d8c27a,#7f8a4a)"></div>
  <span class="icon-dot"><svg width="18" height="18" viewBox="0 0 18 18"><circle cx="11" cy="3" r="2" fill="#fff"/><path d="M4 8l4-3 3 3 3 1M8 5l-1 6 4 2-1 4M7 11l-3 5" stroke="#fff" stroke-width="1.8" fill="none"/></svg></span>
  <h3>Dolorem ipsum quia dolor</h3><p>Ipsum is simply dummy text of the printing and type page when</p>
  <div class="meta"><svg width="18" height="18" viewBox="0 0 20 20"><path d="M10 2l2.4 5.2 5.6.6-4.2 3.8 1.2 5.6L10 14.4 5 17.2l1.2-5.6L2 7.8l5.6-.6z" fill="none" stroke="#999" stroke-width="1.4"/></svg><svg width="18" height="18" viewBox="0 0 20 20"><rect x="2" y="4" width="16" height="14" fill="none" stroke="#999" stroke-width="1.4"/><path d="M2 8h16" stroke="#999" stroke-width="1.4"/></svg><svg width="18" height="18" viewBox="0 0 20 20"><circle cx="10" cy="6" r="4" fill="none" stroke="#999" stroke-width="1.4"/><path d="M3 19c0-5 3-7 7-7s7 2 7 7" fill="none" stroke="#999" stroke-width="1.4"/></svg></div>
</article>

<section class="feelings">
  <h2 class="section-title" style="top:68px">Feelings</h2>
  <article class="feel-card" style="left:91px">
    <div class="photo" role="img" aria-label="Stressed man holding his head at a laptop" style="background:linear-gradient(150deg,#9a8f86,#4f4a47)"><span class="smile"><svg width="20" height="20" viewBox="0 0 20 20"><circle cx="10" cy="10" r="8" fill="none" stroke="#fff" stroke-width="1.6"/><circle cx="7" cy="8" r="1" fill="#fff"/><circle cx="13" cy="8" r="1" fill="#fff"/><path d="M6 12c2 3 6 3 8 0" fill="none" stroke="#fff" stroke-width="1.6"/></svg></span></div>
    <div class="feel-meta"><span class="date">Dec 03</span><span class="count"><svg width="16" height="12" viewBox="0 0 16 12"><rect x="1" y="1" width="14" height="8" rx="2" fill="none" stroke="#fff" stroke-width="1.3"/></svg></span></div>
    <h3>Neque porro quisquam dolorem</h3><p>It has survived not only five centuries, but also the leap into electronic typesetting,</p><a>View More »</a>
  </article>
  <article class="feel-card" style="left:439px">
    <div class="photo" role="img" aria-label="Joyful woman with headphones dancing" style="background:linear-gradient(150deg,#8a7a6e,#d9c9b8)"><span class="smile"><svg width="20" height="20" viewBox="0 0 20 20"><circle cx="10" cy="10" r="8" fill="none" stroke="#fff" stroke-width="1.6"/><circle cx="7" cy="8" r="1" fill="#fff"/><circle cx="13" cy="8" r="1" fill="#fff"/><path d="M6 12c2 3 6 3 8 0" fill="none" stroke="#fff" stroke-width="1.6"/></svg></span></div>
    <div class="feel-meta"><span class="date">Dec 03</span><span class="count"><svg width="16" height="12" viewBox="0 0 16 12"><rect x="1" y="1" width="14" height="8" rx="2" fill="none" stroke="#fff" stroke-width="1.3"/></svg></span></div>
    <h3>Porro quisquam est qui</h3><p>It has survived not only five centuries, but also the leap into electronic typesetting,</p><a>View More »</a>
  </article>
  <article class="feel-card" style="left:793px">
    <div class="photo" role="img" aria-label="Couple in winter coats among evening city lights" style="background:linear-gradient(150deg,#5a3b2a,#c08a4a)"><span class="smile"><svg width="20" height="20" viewBox="0 0 20 20"><circle cx="10" cy="10" r="8" fill="none" stroke="#fff" stroke-width="1.6"/><circle cx="7" cy="8" r="1" fill="#fff"/><circle cx="13" cy="8" r="1" fill="#fff"/><path d="M6 12c2 3 6 3 8 0" fill="none" stroke="#fff" stroke-width="1.6"/></svg></span></div>
    <div class="feel-meta"><span class="date">Dec 03</span><span class="count"><svg width="16" height="12" viewBox="0 0 16 12"><rect x="1" y="1" width="14" height="8" rx="2" fill="none" stroke="#fff" stroke-width="1.3"/></svg></span></div>
    <h3>Dolorem ipsum quia dolor</h3><p>It has survived not only five centuries, but also the leap into electronic typesetting,</p><a>View More »</a>
  </article>
</section>

<footer class="site-footer">
  <div class="newsletter"><h2>Newsletter</h2><span class="field">email@example.com</span><span class="submit">SUBSCRIBE</span></div>
  <div class="footer-brand">Bright<br>Years<br>Ahead</div>
  <div class="footer-col" style="left:368px"><h4>Information</h4><ul><li>Privacy Policy</li><li>Login</li><li>Advanced Search</li><li>Contact Us</li></ul></div>
  <div class="footer-col" style="left:623px"><h4>Contact Us</h4><p>Address : 48 Larkspur Lane, Suite 12<br>Maple Bay, CA 90000<br>Phone : +1 (555) 014-2290<br>Email : hello@brightyearsahead.blog</p></div>
  <div class="footer-col" style="left:937px"><h4>Follow us out there</h4><div class="social"><span></span><span></span><span></span></div></div>
  <div class="footer-rule"></div>
  <div class="copyright">Copyright © 2018. All Rights Reserved</div>
</footer>

</body>
</html>
```